Up to the Challenge - PPT Template with Splash Slide

We are looking for a PPT template that has 4 slides.
1. Splash slide (Creative, fun, no content, a visual representation of the theme)
2. Section header slide
3. Content Slide
4. Content Slide, another design option
The theme is 'UP to the Challenge'. The design should reflect this theme.
The colors should be in Purple (#864B99), Blue (#0A80C2), and Green (#52B054).

```html
<!DOCTYPE html>
<html lang="en">
<head>
<meta charset="utf-8">
<title>Up to the Challenge – Global Summit Deck</title>
<link href="https://fonts.googleapis.com/css2?family=Zilla+Slab:wght@700&family=Montserrat:ital,wght@0,400;0,500;0,600;0,700;1,400&display=swap" rel="stylesheet">
<style>
:root{
  --purple:#864B99;
  --blue:#0A80C2;
  --green:#52B054;
  --ink:#1d1d1f;
  --muted:#7a7a7a;
  --page:#d9dbde;
  --white:#ffffff;
  --rule:#8fb9d8;
}
*{box-sizing:border-box;margin:0;padding:0}
html,body{width:1200px;height:3267px;overflow:hidden}
body{background:var(--page);font-family:"Montserrat",sans-serif;color:var(--ink);position:relative}
.slide{position:absolute;left:184px;width:832px;height:467px;background:var(--white);overflow:hidden}
.abs{position:absolute}
.slab{font-family:"Zilla Slab",serif;font-weight:700}
.photo{position:absolute}

/* footer */
.footer-site{position:absolute;left:16px;top:435px;font-size:8px;letter-spacing:1.6px;font-weight:600;color:var(--ink)}
.footer-rule{position:absolute;left:96px;right:190px;top:440px;height:1px;background:var(--rule)}
.footer-copy{position:absolute;left:652px;top:436px;font-size:5px;color:var(--ink)}
.footer-page{position:absolute;left:800px;top:434px;width:14px;height:12px;background:var(--purple);color:#fff;font-size:7px;font-weight:700;text-align:center;line-height:12px}

/* slide 1 */
.cover{top:138px}
.cover .photo{inset:0;background:radial-gradient(circle at 72% 45%,#3a8f8a 0%,#2a4f8c 28%,#1b2a6e 55%,#0b1240 100%)}
.cover-kicker{left:51px;top:68px;font-size:22px;color:#fff}
.cover-title{left:51px;top:90px;font-size:58px;line-height:1;color:#fff}
.cover-sub{left:51px;top:153px;font-size:36px;color:#fff}
.cover-bar{left:42px;top:249px;width:5px;height:79px;background:var(--green)}
.cover-label{left:57px;top:255px;font-size:23px;font-weight:700;color:#fff}
.cover-lede{left:57px;top:286px;width:300px;font-size:13px;font-style:italic;color:#fff;line-height:1.3}
.cover-date{left:42px;top:393px;font-size:18px;font-weight:700;color:#fff}

/* slide 2 */
.section{top:646px;background:#e8e9ea}
.section .photo{inset:0;background:radial-gradient(circle at 55% 50%,#f3f4f5 0%,#dcdee0 60%,#cfd1d3 100%)}
.agenda-box{left:199px;top:88px;width:501px;height:289px;background:var(--green);opacity:.95}
.section-tag{left:88px;top:179px;width:224px;height:108px;background:var(--purple);color:#fff;font-size:35px;display:flex;align-items:center;justify-content:center}
.tick-a{left:105px;top:165px;width:13px;height:27px;background:var(--blue)}
.tick-b{left:256px;top:275px;width:13px;height:27px;background:var(--blue)}
.agenda{left:341px;width:300px}
.agenda h3{font-size:15px;font-weight:600;color:var(--ink)}
.agenda p{font-size:8.5px;color:#fff;line-height:1.25;padding-left:20px}

/* slide 3 */
.content-a{top:1156px}
.center-title{left:0;right:0;top:46px;text-align:center;font-size:34px}
.center-rule{left:390px;top:92px;width:52px;height:4px;background:var(--green)}
.center-copy{left:86px;width:660px;text-align:center;font-size:11.5px;color:var(--muted);line-height:1.35}
.band{top:216px;height:167px;color:#fff;padding:26px 18px}
.band h3{font-size:25px;margin-bottom:8px}
.band p{font-size:11.2px;line-height:1.2}
.band-blue{left:74px;width:219px;background:var(--blue)}
.band-purple{left:539px;width:219px;background:var(--purple)}
.band-photo{left:293px;top:216px;width:246px;height:167px;background:radial-gradient(circle at 50% 40%,#d9d9d9 0%,#8c8c8c 50%,#3e3e3e 100%)}

/* slide 4 */
.content-b{top:1660px}
.stack-title{left:43px;top:38px;font-size:37px;line-height:1}
.stack-rule{left:43px;top:174px;width:36px;height:4px;background:var(--green)}
.stack-copy{left:43px;width:120px;font-size:10.5px;color:var(--muted);line-height:1.22}
.city-photo{left:184px;top:0;width:294px;height:467px;background:linear-gradient(180deg,#5b8fc4 0%,#a9c6e3 40%,#e8c5c0 75%,#d9dde3 100%)}
.feature-icon{left:445px;width:62px;height:62px;display:flex;align-items:center;justify-content:center}
.feature{left:535px;width:270px}
.feature h3{font-size:18.5px;font-weight:700;margin-bottom:3px}
.feature p{font-size:10.5px;color:var(--muted);line-height:1.22}

/* slide 5 */
.content-c{top:2159px}
.left-title{left:27px;top:20px;font-size:35px}
.left-rule{left:27px;top:70px;width:60px;height:4px;background:var(--green)}
.cycle{left:305px;top:132px}
.step{width:175px;font-size:8.8px;color:var(--muted);line-height:1.25}
.step h4{font-size:15.5px;font-weight:600;margin-bottom:2px}
.step-left{left:105px;text-align:right}
.step-right{left:552px}

/* slide 6 */
.closing{top:2663px}
.closing-photo{left:0;top:69px;width:388px;height:332px;background:linear-gradient(180deg,#8a97a6 0%,#6b7482 55%,#c9cbcf 80%,#9aa0a8 100%)}
.bar-blue{left:49px;top:37px;width:13px;height:57px;background:var(--blue)}
.bar-green{left:323px;top:369px;width:13px;height:57px;background:var(--green)}
.thanks{left:431px;top:126px;font-size:68px}
.contact{left:441px;display:flex;align-items:center;font-size:13.5px;color:#333;line-height:1.22}
.contact svg{width:24px;height:24px;flex:none}
.contact .sep{width:2px;height:28px;background:var(--ink);margin:0 12px 0 14px}
</style>
</head>
<body>

<!-- Slide 1: splash -->
<section class="slide cover">
  <div class="photo" role="img" aria-label="Hand reaching toward a glowing network globe"></div>
  <p class="abs slab cover-kicker">Up to the</p>
  <h1 class="abs slab cover-title">Challenge ?</h1>
  <p class="abs slab cover-sub">Global Summit</p>
  <div class="abs cover-bar"></div>
  <p class="abs cover-label">Presentation</p>
  <p class="abs cover-lede">Lorem ipsum dolor sit amet, consectetuer adipiscing elit, sed diam nonum</p>
  <p class="abs cover-date">30th June 2024</p>
</section>

<!-- Slide 2: section header -->
<section class="slide section">
  <div class="photo" role="img" aria-label="Faint wireframe globe on light grey"></div>
  <div class="abs agenda-box"></div>
  <div class="abs tick-a"></div>
  <div class="abs section-tag slab">Discussion:</div>
  <div class="abs tick-b"></div>
  <div class="abs agenda" style="top:111px"><h3>1. Lorem ipsum</h3><p>Lorem ipsum dolor sit amet, consectetuer adipiscing elit, sed diam nonummy nibh euismod tincid</p></div>
  <div class="abs agenda" style="top:180px"><h3>2. Lorem ipsum</h3><p>Lorem ipsum dolor sit amet, consectetuer adipiscing elit, sed diam nonummy nibh euismod tincid</p></div>
  <div class="abs agenda" style="top:248px"><h3>3. Lorem ipsum</h3><p>Lorem ipsum dolor sit amet, consectetuer adipiscing elit, sed diam nonummy nibh euismod tincid</p></div>
  <div class="abs agenda" style="top:315px"><h3>4. Lorem ipsum</h3><p>Lorem ipsum dolor sit amet, consectetuer adipiscing elit, sed diam nonummy nibh euismod tincid</p></div>
  <p class="footer-site">summitway.com</p><div class="footer-rule"></div>
  <p class="footer-copy">Copyright © 2024 Company name. All rights reserved.</p><p class="footer-page">2</p>
</section>

<!-- Slide 3: content -->
<section class="slide content-a">
  <h2 class="abs slab center-title">Text Added Here</h2>
  <div class="abs center-rule"></div>
  <p class="abs center-copy" style="top:114px">Lorem ipsum dolor sit amet, consectetuer adipiscing elit, sed diam nonummy nibh euismod tincidunt ut laoreet dolore magna aliquam erat volutpat.</p>
  <p class="abs center-copy" style="top:159px">Ut wisi enim ad minim veniam, quis nostrud exerci tation ullamcorper suscipit lobortis nisl ut aliquip ex ea commodo consequat. Duis autem vel eum iriure dolor in hendrerit i</p>
  <div class="abs band band-blue"><h3 class="slab">Text Here</h3><p>Lorem ipsum dolor sit amet, consectetuer adipiscing elit, sed diam nonummy nibh euismod tincidunt ut laoreet dolore magna aliquam erat volutpat.</p></div>
  <div class="abs band-photo" role="img" aria-label="Globe of flags presented on a silver tray over a world map"></div>
  <div class="abs band band-purple"><h3 class="slab">Text Here</h3><p>Lorem ipsum dolor sit amet, consectetuer adipiscing elit, sed diam nonummy nibh euismod tincidunt ut laoreet dolore magna aliquam erat volutpat.</p></div>
  <p class="footer-site">summitway.com</p><div class="footer-rule"></div>
  <p class="footer-copy">Copyright © 2024 Company name. All rights reserved.</p><p class="footer-page">3</p>
</section>

<!-- Slide 4: content, alternate -->
<section class="slide content-b">
  <h2 class="abs slab stack-title">Text<br>Added<br>Here</h2>
  <div class="abs stack-rule"></div>
  <p class="abs stack-copy" style="top:192px">Lorem ipsum dolor sit amet, consec-tetuer adipiscing elit, sed diam nonummy nibh euismod tincidunt ut laoreet dolore magna aliquam erat volutpat.</p>
  <p class="abs stack-copy" style="top:320px">Ut wisi enim ad minim veniam, quis nostrud exerci tation ullamcorper suscipit lobortis nisl ut aliquip ex ea commodo</p>
  <p class="footer-site">summitway.com</p><div class="footer-rule"></div>
  <div class="photo city-photo" role="img" aria-label="Businessman facing a city skyline under a sky with a world map"></div>
  <div class="abs feature-icon" style="top:77px;background:var(--blue)">
    <svg width="40" height="40" viewBox="0 0 40 40" fill="#fff"><circle cx="20" cy="13" r="5"/><circle cx="10" cy="16" r="4"/><circle cx="30" cy="16" r="4"/><path d="M11 31c0-6 4-10 9-10s9 4 9 10z"/><path d="M3 30c0-5 3-8 7-8 1.5 0 2.5.4 3 .8C10.5 25 9.5 27.5 9.5 30z"/><path d="M37 30c0-5-3-8-7-8-1.5 0-2.5.4-3 .8 2.5 2.2 3.5 4.7 3.5 7.2z"/></svg>
  </div>
  <div class="abs feature" style="top:77px"><h3>We Before Me</h3><p>ipsum dolor sit amet, cons ectetuer adipiscing elit, sed diam nonummy nibh euismod tincidunt ut laoreet</p></div>
  <div class="abs feature-icon" style="top:202px;background:var(--green)">
    <svg width="40" height="40" viewBox="0 0 40 40" fill="none" stroke="#fff" stroke-width="2"><circle cx="14" cy="8" r="3.5"/><circle cx="26" cy="8" r="3.5"/><path d="M9 36V15h10v21M21 36V15h10v21M14 22v14M26 22v14"/></svg>
  </div>
  <div class="abs feature" style="top:202px"><h3>We Are Good People</h3><p>ipsum dolor sit amet, cons ectetuer adipiscing elit, sed diam nonummy nibh euismod ut laoreet dolore magna aliquam erat volutpat.</p></div>
  <div class="abs feature-icon" style="top:325px;background:var(--purple)">
    <svg width="40" height="40" viewBox="0 0 40 40"><path d="M22 20c-4-3-7-5.5-7-9a4 4 0 0 1 7-2.5A4 4 0 0 1 29 11c0 3.5-3 6-7 9z" fill="#fff"/><path d="M4 27h7l6 3h10c2 0 2 3 0 3h-8M11 27l3-3h6l3 2h8l4-2" fill="none" stroke="#fff" stroke-width="2"/></svg>
  </div>
  <div class="abs feature" style="top:325px"><h3>We Work with Heart</h3><p>ipsum dolor sit amet, cons ectetuer adipiscing elit, sed diam nonummy nibh euismod tincidunt</p></div>
  <p class="footer-copy">Copyright © 2024 Company name. All rights reserved.</p><p class="footer-page">2</p>
</section>

<!-- Slide 5: cycle -->
<section class="slide content-c">
  <h2 class="abs slab left-title">Text Added Here</h2>
  <div class="abs left-rule"></div>
  <svg class="abs cycle" width="224" height="224" viewBox="0 0 224 224">
    <path d="M110 0A112 112 0 0 0 0 110H56A56 56 0 0 1 110 56Z" fill="var(--purple)"/>
    <path d="M114 0A112 112 0 0 1 224 110H168A56 56 0 0 0 114 56Z" fill="var(--green)"/>
    <path d="M224 114A112 112 0 0 1 114 224V168A56 56 0 0 0 168 114Z" fill="var(--ink)"/>
    <path d="M0 114A112 112 0 0 0 110 224V168A56 56 0 0 1 56 114Z" fill="var(--blue)"/>
    <g fill="none" stroke="#fff" stroke-width="2">
      <circle cx="58" cy="48" r="10"/><circle cx="58" cy="48" r="4"/>
      <circle cx="166" cy="48" r="10"/><path d="M161 53l10-10"/>
      <circle cx="166" cy="176" r="10"/><circle cx="166" cy="176" r="4"/>
      <rect x="48" y="168" width="20" height="16" rx="2"/><path d="M54 176h8"/>
    </g>
    <text x="112" y="108" text-anchor="middle" font-family="Montserrat, sans-serif" font-weight="700" font-size="19" fill="var(--ink)">Text</text>
    <text x="112" y="130" text-anchor="middle" font-family="Montserrat, sans-serif" font-weight="700" font-size="19" fill="var(--ink)">Added</text>
  </svg>
  <div class="abs step step-left" style="top:132px"><h4 style="color:var(--purple)">Text Here</h4>Lorem ipsum dolor sit amet, consectetuer adipiscing elit, sed diammy nibh euismod tincidunt ut laoreet dolore</div>
  <div class="abs step step-right" style="top:132px"><h4 style="color:var(--green)">Text Here</h4>Lorem ipsum dolor sit amet, consectetuer adipiscing elit, sed diammy nibh euismod tincidunt ut laoreet dolore</div>
  <div class="abs step step-left" style="top:292px"><h4 style="color:var(--blue)">Text Here</h4>Lorem ipsum dolor sit amet, consectetuer adipiscing elit, sed diammy nibh euismod tincidunt ut laoreet dolore</div>
  <div class="abs step step-right" style="top:292px"><h4 style="color:var(--ink)">Text Here</h4>Lorem ipsum dolor sit amet, consectetuer adipiscing elit, sed diammy nibh euismod tincidunt ut laoreet dolore</div>
  <p class="footer-site">summitway.com</p><div class="footer-rule"></div>
  <p class="footer-copy">Copyright © 2024 Company name. All rights reserved.</p><p class="footer-page">2</p>
</section>

<!-- Slide 6: closing -->
<section class="slide closing">
  <div class="photo closing-photo" role="img" aria-label="Businessman with binoculars before a world map above a city and a desk"></div>
  <div class="abs bar-blue"></div>
  <div class="abs bar-green"></div>
  <h2 class="abs slab thanks">Thank You</h2>
  <div class="abs contact" style="top:233px">
    <svg viewBox="0 0 24 24"><path d="M6 3l4 4-2 3c1 2 4 5 6 6l3-2 4 4-3 3C10 21 3 14 3 6z" fill="var(--purple)"/></svg>
    <span class="sep"></span><span>+1 555 0142 2280<br>+1 555 0142 2280</span>
  </div>
  <div class="abs contact" style="top:284px">
    <svg viewBox="0 0 24 24"><path d="M2 10L22 3l-6 19-4-8z" fill="var(--green)"/></svg>
    <span class="sep"></span><span>www.summitway.com<br>hello@summitway.com</span>
  </div>
  <div class="abs contact" style="top:331px">
    <svg viewBox="0 0 24 24"><path d="M12 3L1 13h3v8h6v-6h4v6h6v-8h3z" fill="var(--blue)"/></svg>
    <span class="sep"></span><span>88 Harbor Lane, Millbrook,<br>Westland, 40219.</span>
  </div>
</section>

</body>
</html>
```